Gift voucher for a photo shoot, folding card DIN long (21 x 9.8 cm)

Hello, I'm a professional photographer and need a new design for my gift voucher card for a photo shoot. The design should be applicable to all types of photo shoots (neutral). I prefer a sophisticated design. The folded card should be printed on both sides.
My data should be included: Logo, Address: Wendtholzer Strße 27, 07549 Gera, Email: fotograf@malteburgardt.eu, Website: www.malteburgardt.eu Tel.: 0173 / 4958302
Updates

Please design the folding card in DIN long format (105 x 210 mm, landscape format). The card should open horizontally. Please design the front with the words "Gift voucher for you" and my logo. Please make the logo small – the words "Gift voucher" should be in the foreground.
The colors - use elegant gray with gold or white font color.
The inside should contain the words: Photo shoot for ........ worth .....€, as well as my logo.
My contact details should be on the back.

Target Market(s)

Private customer

Colors

Designer to choose only greyscale colors for use in the design.

Requirements
Must have
• Noble appearance, a gift voucher that one likes to give away, words: Gift voucher for you, photo shoot for ..., worth .......€
Nice to have
• Noble appearance of the gift voucher, a gift voucher that you like to give away
Should not have
• no pictures

```html
<!DOCTYPE html>
<html lang="en">
<head>
<meta charset="utf-8">
<title>Gift Voucher – Photo Shoot</title>
<link rel="stylesheet" href="https://fonts.googleapis.com/css2?family=Cormorant+Garamond:wght@500&family=Montserrat:wght@300;400&display=swap">
<style>
  :root {
    --backdrop: #ede5e0;
    --panel-light: #e7dfd9;
    --panel-grey: #b2aaa5;
    --gold-dark: #85705b;
    --gold-light: #b39d83;
    --gold-line: #b89f82;
    --ink: #1f1c1a;
    --white: #f7f3ef;
  }
  * { margin: 0; padding: 0; box-sizing: border-box; }
  html, body {
    width: 1200px;
    height: 900px;
    overflow: hidden;
    background: var(--backdrop);
  }
  .voucher {
    position: absolute;
    left: 153px;
    top: 224px;
    width: 895px;
    height: 451px;
    border-radius: 22px;
    overflow: hidden;
    display: flex;
    box-shadow: 0 3px 8px rgba(90, 70, 55, 0.18);
  }
  .voucher-front {
    position: relative;
    width: 447px;
    height: 100%;
    background: var(--panel-light);
  }
  .voucher-title {
    position: absolute;
    left: 50px;
    top: 62px;
    font-family: "Cormorant Garamond", serif;
    font-weight: 500;
    font-size: 84px;
    line-height: 68px;
    letter-spacing: -0.5px;
    background: linear-gradient(90deg, var(--gold-dark), var(--gold-light));
    -webkit-background-clip: text;
    background-clip: text;
    color: transparent;
  }
  .voucher-fields {
    position: absolute;
    left: 50px;
    top: 334px;
    font-family: "Montserrat", sans-serif;
    font-weight: 400;
    font-size: 20px;
    line-height: 30px;
    color: var(--ink);
  }
  .voucher-brand {
    position: relative;
    flex: 1;
    height: 100%;
    background: var(--panel-grey);
  }
  .brand-frame {
    position: absolute;
    left: 35px;
    top: 23px;
    width: 391px;
    height: 401px;
    border: 1.5px solid var(--gold-line);
  }
  .brand-mark {
    position: absolute;
    left: 150px;
    top: 134px;
    width: 162px;
    height: 162px;
  }
  .brand-name {
    position: absolute;
    left: 0;
    right: 18px;
    top: 355px;
    text-align: center;
    font-family: "Montserrat", sans-serif;
    font-weight: 300;
    color: var(--white);
  }
  .brand-name .name-main {
    display: block;
    font-size: 23px;
    letter-spacing: 2px;
  }
  .brand-name .name-sub {
    display: block;
    margin-top: 4px;
    font-size: 11px;
    letter-spacing: 1px;
  }
</style>
</head>
<body>
  <div class="voucher">
    <section class="voucher-front">
      <h1 class="voucher-title">Gift<br>Voucher<br>for You</h1>
      <p class="voucher-fields">Photo Shoot for ……………€<br>worth …..</p>
    </section>
    <section class="voucher-brand">
      <div class="brand-frame"></div>
      <svg class="brand-mark" viewBox="0 0 162 162" aria-hidden="true">
        <circle cx="81" cy="81" r="78" fill="none" stroke="var(--gold-line)" stroke-width="2"/>
      </svg>
      <p class="brand-name">
        <span class="name-main">PHOTOGRAPHER</span>
        <span class="name-sub">PHOTOGRAPHY</span>
      </p>
    </section>
  </div>
</body>
</html>
```